Vantrel Consulting Business card design.

See our website www.vantrelconsulting.com which will give you a good idea of what we are about. The font is called 'Play'.

I'd like a standout business card in keeping with the themes and branding on the website

Target Market(s)

professionals. HR directors

Industry/Entity Type

Business

Contact Information for Business Card

Vantrel Consulting PO Box 3917 Marrowdene NSW 2279 1300 584 316 Gareth Lindqvane Principal email: career@vantrelconsulting.com ABN: 41293087614

Other font styles liked:
• Play

Requirements
Must have
• Must have same design colours and branding as website.
• On back I'd prefer a list of the things we do which appears below the name at the header on the website

```html
<!DOCTYPE html>
<html lang="en">
<head>
<meta charset="utf-8">
<title>Vantrel Consulting — Business Card</title>
<link href="https://fonts.googleapis.com/css2?family=Play:wght@400;700&display=swap" rel="stylesheet">
<style>
  :root {
    --navy: #0d2034;
    --blue: #3a8fd0;
    --white: #ffffff;
    --page: #ffffff;
    --card-edge: #d4d6d9;
  }
  * { margin: 0; padding: 0; box-sizing: border-box; }
  html, body {
    width: 1200px;
    height: 1000px;
    overflow: hidden;
    background: var(--page);
    font-family: "Play", sans-serif;
  }
  .canvas { position: relative; width: 1200px; height: 1000px; }

  .card { position: absolute; left: 327px; width: 550px; height: 343px; }

  /* Front */
  .card--front { top: 144px; background: var(--navy); }
  .front-brand {
    position: absolute; left: 0; right: 0; top: 272px; top: 128px;
    text-align: center;
  }
  .wordmark {
    color: var(--white);
    font-size: 41px;
    letter-spacing: 0.5px;
    line-height: 1;
    white-space: nowrap;
  }
  .services {
    margin-top: 16px;
    color: var(--blue);
    font-size: 12px;
    letter-spacing: 1px;
    white-space: nowrap;
  }
  .services .sep { color: var(--white); margin: 0 5px; }

  /* Back */
  .card--back {
    top: 513px;
    background: var(--white);
    border: 1px solid var(--card-edge);
  }
  .contact {
    position: absolute; right: 39px; top: 45px;
    text-align: right;
  }
  .contact-name {
    color: var(--navy);
    font-size: 18px;
    letter-spacing: 1.2px;
    line-height: 1;
  }
  .contact-phone {
    margin-top: 18px;
    display: flex; align-items: center; justify-content: flex-end;
    color: var(--blue);
    font-size: 42px;
    line-height: 1;
  }
  .contact-phone svg { width: 32px; height: 32px; margin-right: 2px; }
  .contact-email {
    margin-top: 4px;
    color: var(--blue);
    font-size: 13px;
    letter-spacing: 0.6px;
  }
  .company-band {
    position: absolute; left: 0; right: 0; bottom: 0; height: 135px;
    background: var(--navy);
    padding: 26px 0 0 39px;
    color: var(--white);
  }
  .band-wordmark { font-size: 19px; line-height: 1; letter-spacing: 0.3px; }
  .company-details {
    margin-top: 2px;
    font-size: 13px;
    line-height: 14.5px;
    letter-spacing: 0.6px;
    font-style: normal;
  }
</style>
</head>
<body>
<div class="canvas">

  <section class="card card--front" aria-label="Card front">
    <div class="front-brand">
      <div class="wordmark">VANTREL CONSULTING</div>
      <div class="services">Search &amp; Select<span class="sep">I</span>Career<span class="sep">I</span>Coaching<span class="sep">I</span>Leadership<span class="sep">I</span>Outplacement</div>
    </div>
  </section>

  <section class="card card--back" aria-label="Card back">
    <div class="contact">
      <div class="contact-name">GARETH LINDQVANE</div>
      <div class="contact-phone">
        <svg viewBox="0 0 24 24" aria-hidden="true"><path fill="#0d2034" d="M6.6 2.2c.6-.3 1.3-.1 1.6.5l2.1 3.7c.3.6.2 1.3-.3 1.7L8.3 9.5c1.1 2.5 3.3 4.7 5.9 5.9l1.4-1.7c.4-.5 1.1-.6 1.7-.3l3.7 2.1c.6.3.8 1 .5 1.6l-1.1 2.3c-.5 1-1.5 1.6-2.6 1.5C9.8 20.3 3.7 14.2 3.1 6.4c-.1-1.1.5-2.1 1.5-2.6z"/></svg>
        <span>1300 584 316</span>
      </div>
      <div class="contact-email">career@vantrelconsulting.com</div>
    </div>
    <div class="company-band">
      <div class="band-wordmark">VANTREL CONSULTING</div>
      <address class="company-details">
        PO Box 3917<br>
        Marrowdene NSW 2279<br>
        ABN 41293087614<br>
        www.vantrelconsulting.com
      </address>
    </div>
  </section>

</div>
</body>
</html>
```